Steadfast sons flyer

Benefits of prayer
- Prayer connects you to the God of fullness. Gal. 6:8
- Prayer places you cares on the Lord. 1 Peter 5:7, Matt. 11:28
- Prayer makes you fruitful in the vineyard of the Lord-this brings honour and glory. John 15:2
- Through prayer you exercise your Kingly authority. Matt. 16:19, 18:19.
- Prayer transforms you to be like Him. Luke 9:29.
- Prayer quickens divine inheritance. Luke 5:3-6
- Prayer will stir divine potentials in you. 2 Tim. 1:6
- And many more!

Experience the might and possibilities of prayer.

Join the Steadfast Sons Ministry!

```html
<!DOCTYPE html>
<html lang="en">
<head>
<meta charset="utf-8">
<title>Steadfast Sons Ministry – Prayer Flyer</title>
<link rel="stylesheet" href="https://fonts.googleapis.com/css2?family=Montserrat:wght@400;600;900&family=Oswald:wght@300;400&family=Playfair+Display:ital,wght@1,900&display=swap">
<style>
  :root {
    --stage: #f2f3f5;
    --blue: #1f4fa3;
    --blue-band: #1d4690;
    --green: #5bb135;
    --green-light: #7cc242;
    --green-dark: #3f8a26;
    --white: #ffffff;
    --haze-top: #f4e9ee;
    --haze-mid: #a9bfd0;
    --crowd-dark: #172638;
  }
  * { margin: 0; padding: 0; box-sizing: border-box; }
  html, body { width: 1200px; height: 1000px; overflow: hidden; background: var(--stage); }
  .canvas { position: relative; width: 1200px; height: 1000px; }

  .flyer {
    position: absolute; left: 300px; top: 80px; width: 600px; height: 840px;
    overflow: hidden; box-shadow: 0 10px 30px rgba(0,0,0,.25);
    font-family: "Montserrat", sans-serif;
  }
  .flyer__photo {
    position: absolute; inset: 0;
    background:
      radial-gradient(ellipse at 50% 18%, rgba(255,255,255,.9), rgba(255,255,255,0) 55%),
      linear-gradient(180deg, var(--haze-top) 0%, #e9dce6 30%, var(--haze-mid) 52%, #4f6a82 68%, var(--crowd-dark) 100%);
  }
  .flyer__art { position: absolute; inset: 0; }

  .brand {
    position: absolute; left: 0; right: 0; top: 156px;
    display: flex; justify-content: center; align-items: center; gap: 10px;
  }
  .brand__dot { width: 32px; height: 32px; border-radius: 50%; background: var(--blue); }
  .brand__name { color: var(--blue); font-weight: 600; font-size: 19px; }

  .headline {
    position: absolute; left: 0; right: 0; top: 212px; text-align: center;
    font-family: "Oswald", sans-serif; font-weight: 300; color: var(--green);
    font-size: 104px; line-height: 1; letter-spacing: 14px; padding-left: 14px;
  }
  .ribbon__text {
    position: absolute; left: 185px; width: 255px; top: 427px; text-align: center;
    color: var(--white); font-size: 13px; letter-spacing: 2px;
  }
  .join {
    position: absolute; left: 0; right: 0; top: 474px; text-align: center;
    color: var(--white); font-weight: 900; font-size: 74px; line-height: 1;
  }
  .join__sub {
    position: absolute; left: 0; right: 0; top: 556px; text-align: center;
    color: transparent; -webkit-text-stroke: 1px var(--white);
    font-weight: 400; font-size: 25px; line-height: 1.2; letter-spacing: 1px;
  }
  .benefits__title {
    position: absolute; left: 0; right: 0; top: 598px; text-align: center;
    font-family: "Playfair Display", serif; font-style: italic; font-weight: 900;
    color: var(--white); font-size: 27px; line-height: 1.3;
  }
  .benefits {
    position: absolute; left: 8px; right: 6px; top: 636px;
    display: grid; grid-template-columns: 1fr 1fr; row-gap: 2px;
  }
  .benefit { height: 40px; display: flex; flex-direction: column; justify-content: flex-end; }
  .benefit__ref { color: var(--white); font-weight: 600; font-size: 12px; padding: 0 6px 2px; }
  .benefit--right .benefit__ref { text-align: right; }
  .benefit__band {
    display: flex; align-items: center; gap: 6px; min-height: 20px;
    padding: 1px 8px; color: var(--white); font-size: 10.5px; line-height: 1.15;
  }
  .benefit__band::before {
    content: ""; flex: none; width: 7px; height: 7px; border-radius: 50%; background: var(--white);
  }
  .benefit--left .benefit__band { background: var(--blue-band); }
  .benefit--right .benefit__band { background: var(--green); }
  .benefit--tall { height: 46px; }
  .benefit--tall .benefit__band { min-height: 26px; }
</style>
</head>
<body>
<main class="canvas">
  <article class="flyer">
    <div class="flyer__photo" role="img" aria-label="Worship crowd with raised hands under stage lights"></div>

    <svg class="flyer__art" width="600" height="840" viewBox="0 0 600 840" aria-hidden="true">
      <defs>
        <path id="arch-text-path" d="M78 280 A222 200 0 0 1 522 280"/>
      </defs>
      <path d="M19 326 V290 A281 262 0 0 1 581 290 V326" fill="none" stroke="var(--blue)" stroke-width="6"/>
      <path d="M31 326 V290 A269 250 0 0 1 569 290 V326" fill="none" stroke="var(--blue)" stroke-width="2"/>
      <text font-family="Montserrat, sans-serif" font-size="25" font-weight="400" fill="var(--green)">
        <textPath href="#arch-text-path" startOffset="50%" text-anchor="middle">EXPERIENCE THE MIGHT &amp; POSSIBILITIES OF</textPath>
      </text>
      <line x1="209" y1="140" x2="417" y2="140" stroke="var(--blue)" stroke-width="2"/>
      <line x1="209" y1="206" x2="417" y2="206" stroke="var(--blue)" stroke-width="2"/>
      <path d="M14 326 H44 Q64 326 64 350 V374 Q64 398 94 398 M586 326 H556 Q536 326 536 350 V374 Q536 398 506 398"
            stroke="var(--blue)" stroke-width="6" fill="none"/>
      <path d="M160 426 H200 V462 H160 L172 444 Z" fill="var(--green-dark)"/>
      <path d="M465 426 H425 V462 H465 L453 444 Z" fill="var(--green-dark)"/>
      <path d="M185 418 Q312 404 440 418 V456 Q312 442 185 456 Z" fill="var(--green-light)"/>
      <line x1="8" y1="592" x2="594" y2="592" stroke="var(--white)" stroke-width="1.5"/>
    </svg>

    <div class="brand">
      <span class="brand__dot"></span>
      <span class="brand__name">Hall of Song Fellowship</span>
    </div>

    <h1 class="headline">PRAYER</h1>
    <p class="ribbon__text">WE ARE WAITING YOU</p>

    <p class="join">JOIN</p>
    <p class="join__sub">THE STEADFAST SONS MINISTRY!</p>

    <h2 class="benefits__title">Benefits of Prayer:</h2>
    <section class="benefits">
      <div class="benefit benefit--left"><span class="benefit__ref">GAL. 6:8</span><p class="benefit__band">Prayer connects you to the God of fullness.</p></div>
      <div class="benefit benefit--right"><span class="benefit__ref">LUKE 9:29</span><p class="benefit__band">Prayer transforms you to be like Him.</p></div>
      <div class="benefit benefit--left"><span class="benefit__ref">1 PETER 5:7, MATT. 11:28</span><p class="benefit__band">Prayer places you cares on the Lord.</p></div>
      <div class="benefit benefit--right"><span class="benefit__ref">LUKE 5:3-6</span><p class="benefit__band">Prayer quickens divine inheritance.</p></div>
      <div class="benefit benefit--left benefit--tall"><span class="benefit__ref">JOHN 15:2</span><p class="benefit__band">Prayer makes you fruitful in the vineyard of the Lord this brings honour and glory.</p></div>
      <div class="benefit benefit--right benefit--tall"><span class="benefit__ref">2 TIM. 1:6</span><p class="benefit__band">Prayer will stir divine potentials in you.</p></div>
      <div class="benefit benefit--left"><span class="benefit__ref">MATT. 16:19, 18:19.</span><p class="benefit__band">Through prayer you exercise your Kingly authority</p></div>
      <div class="benefit benefit--right"><span class="benefit__ref">&nbsp;</span><p class="benefit__band">And many more!</p></div>
    </section>
  </article>
</main>
</body>
</html>
```